General Dental Office Business Card

I run a private general dental office in southern California, and would like a refresh/redesign of my business card. I focus on quality care rather than volume. The email address on the uploaded current card should be updated to: info@marbleshoredental.example. The current card's logo is a deboss, but I am open to other ideas. The logo can be refreshed, but it is something that's been with me since the beginning of the office, so I wouldn't want a drastic redesign.
Target Market(s)
Adults 18-99, whoever needs dental services
Industry/Entity Type
Healthcare/Dental
Contact Information for Business Card
Name, Address, Phone, email
Colors
Designer to choose colors to be used in the design.
Requirements
Must have
- Logo (Same as original one in the uploaded file), space on back for appointment time/date

```html
<!DOCTYPE html>
<html lang="en">
<head>
<meta charset="utf-8">
<title>Marble Shore Dental – Business Card</title>
<link rel="stylesheet" href="https://fonts.googleapis.com/css2?family=Lato:wght@400&family=Raleway:wght@400;700&display=swap">
<style>
  :root {
    --backdrop: #9a9a9a;
    --card-light: #dedede;
    --ink-dark: #111111;
    --ink-muted: #7a7a7a;
    --rule: #555555;
    --teal-light: #4ec9d1;
    --teal-deep: #3bb6be;
    --white: #ffffff;
  }
  * { margin: 0; padding: 0; box-sizing: border-box; }
  html, body { width: 1200px; height: 1200px; overflow: hidden; }
  body { background: var(--backdrop); position: relative; font-family: "Raleway", sans-serif; }

  .card {
    position: absolute;
    left: 227px;
    width: 747px;
    height: 437px;
    border-radius: 30px;
    overflow: hidden;
  }

  /* Appointment side */
  .card--appointment { top: 150px; background: var(--card-light); }
  .brand-mark {
    position: absolute; left: 83px; top: 90px;
    width: 250px; height: 250px; border-radius: 50%;
    background: var(--white);
    display: flex; align-items: center; justify-content: center; text-align: center;
  }
  .brand-mark__name {
    font-family: "Raleway", sans-serif; font-weight: 700; font-size: 26px;
    line-height: 1.25; color: var(--ink-dark);
  }
  .dentist-name {
    position: absolute; left: 376px; top: 82px;
    font-weight: 700; font-size: 26px; color: var(--ink-dark);
  }
  .dentist-role {
    position: absolute; left: 377px; top: 116px;
    font-size: 18px; color: var(--ink-muted);
  }
  .appointment-field {
    position: absolute; left: 377px;
    display: flex; align-items: flex-end;
    font-size: 17px; color: var(--ink-dark);
  }
  .appointment-field__line {
    display: inline-block; border-bottom: 1px solid var(--rule);
    margin-left: 2px; margin-bottom: 4px;
  }
  .appointment-field--date { top: 161px; }
  .appointment-field--date .appointment-field__line { width: 192px; }
  .appointment-field--time { top: 217px; }
  .appointment-field--time .appointment-field__line { width: 190px; }
  .address {
    position: absolute; left: 379px; top: 274px;
    font-size: 16px; line-height: 22px; color: var(--ink-muted);
  }
  .contact-line {
    position: absolute; left: 379px;
    display: flex; align-items: center; gap: 6px;
    font-size: 16px; color: var(--ink-muted);
  }
  .contact-line svg { width: 14px; height: 14px; fill: var(--ink-dark); }
  .contact-line--phone { top: 331px; }
  .contact-line--email { top: 355px; }

  /* Brand side */
  .card--brand {
    top: 651px;
    background: linear-gradient(135deg, var(--teal-light), var(--teal-deep));
  }
  .brand-title {
    position: absolute; left: 371px; top: 270px;
    font-family: "Lato", sans-serif; font-weight: 400; font-size: 41px;
    line-height: 42px; letter-spacing: 0.5px; color: var(--white);
  }
  .brand-url {
    position: absolute; left: 373px; top: 358px;
    font-size: 21px; color: var(--white);
  }
</style>
</head>
<body>
  <section class="card card--appointment">
    <div class="brand-mark"><span class="brand-mark__name">Marble Shore<br>Dental</span></div>
    <h1 class="dentist-name">Dr. Daniel Reyes</h1>
    <p class="dentist-role">General Dentistry</p>
    <p class="appointment-field appointment-field--date">Date:<span class="appointment-field__line"></span></p>
    <p class="appointment-field appointment-field--time">Time:<span class="appointment-field__line"></span></p>
    <p class="address">1280 Harbor Crest Avenue<br>Seaview, CA 92600</p>
    <p class="contact-line contact-line--phone">
      <svg viewBox="0 0 24 24" aria-hidden="true"><path d="M6.6 10.8a15.2 15.2 0 0 0 6.6 6.6l2.2-2.2a1 1 0 0 1 1-.25 11.4 11.4 0 0 0 3.6.57 1 1 0 0 1 1 1V20a1 1 0 0 1-1 1A17 17 0 0 1 3 4a1 1 0 0 1 1-1h3.5a1 1 0 0 1 1 1c0 1.25.2 2.45.57 3.6a1 1 0 0 1-.25 1z"/></svg>
      (555) 014-2828
    </p>
    <p class="contact-line contact-line--email">
      <svg viewBox="0 0 24 24" aria-hidden="true"><path d="M2 4h20v16H2zm2 2v.5l8 5.5 8-5.5V6zm0 3v9h16V9l-8 5.5z"/></svg>
      info@marbleshoredental.example
    </p>
  </section>

  <section class="card card--brand">
    <h2 class="brand-title">MARBLE<br>SHORE DENTAL</h2>
    <p class="brand-url">www.marbleshoredental.example</p>
  </section>
</body>
</html>
```